Quiet Horizon Splash page

We want a page to educate the facility managers of Office buildings on the wasted lighting that is left on at night time in their buildings. The page should encourage them to reach out to us for ways to reduce/eliminate the wasted lighting.
Part of the motivation is created by showing photographs of city skylines, and highlight specific buildings, and floors in buildings that have lights left on when the light is not needed. We have attached photos of the San Francisco and LA skylines. We have also created a page with youtube videos educating on light pollution. http://www.vexalume.example/education-center-2/vexalume-video-library/
Details:
- We would like a graphic on the page that is the symbol to represent the Quiet Horizon we are working to create.
- The page should be able to segment different cities
- The page should be stand alone with enough information to be valuable, but also should link into more details
- The page should tie into our existing site www.vexalume.example
- The page should motivate people to eliminate their wasted light by contacting us
Updates

Hi all, We have received a number of designs, and some are close to our expectation. We will choose a 1st and 2nd place tomorrow night. Here is more clarification based on the designs being submitted: (Please edit your submission if it does not match with the notes below) 1. This design is Not for a homepage or to represent VexaLume corporately. This design is only to do an interior page that will be the Quiet Horizon initiative. 2. The "Symbol to represent the Quiet Horizon" is a graphic, logo or image that can universally be recognized as representing our Quiet Horizon initiative. This would be used on the webpage and literature we may develop in the future. 3. We expect people visiting this Quiet Horizon page to ask a couple questions. * "What is the Quiet Horizon?" * Is my building causing the wasted lighting (Can I look at a photo of my city {San Francisco, Los Angeles, New York City} and see my building lit up at night? * Is VexaLume creating a Quiet Horizon? (See images from every 6 months of the same city skyline to see how it is changing) 4. The webpage should not focus on the specific capabilities, skills, tools or software of VexaLume. It should only focus on the Who, What, Where, Why, How of creating a Quiet Horizon.

Here are notes to help with the design: - Use our uploaded skyline images. - Highlight a level of light left on in those images. and note, "Is your lighting wasted for hours every night?" - Highlight a dark area of a building in those images and note "We helped create a Quiet Horizon here!" - Add an email address to contact us at the bottom and say, "I want to be part of the Quiet Horizon in my city!""

Hi All Designers, Sorry for the delay while I was traveling the past week. We had 62 designs submitted and we have narrowed it down to 7. We are voting this week on designs that are best and then we will choose First place and Second place awards. Thanks! Milo

Target Market(s)

Owners and managers of large office buildings in Western speaking countries. Generally adult male aged 30-60.

Industry/Entity Type

Education

Requirements
Must have
• Sectioned areas for different cities based on where the person is visiting our website from. Major cities we focus on include: Los Angeles, San Francisco, New York City, Philadelphia
Nice to have
• Graphic or image logo representing the Quiet Horizon.
Should not have
• Do not focus on VexaLume. Focus on the Quiet Horizon initiative.

```html
<!DOCTYPE html>
<html lang="en">
<head>
<meta charset="utf-8">
<title>Quiet Horizon – VexaLume</title>
<link href="https://fonts.googleapis.com/css2?family=Arimo:wght@400;700&display=swap" rel="stylesheet">
<style>
:root{
  --page-bg:#f4f4f4;
  --white:#ffffff;
  --ink:#333333;
  --nav-bg:#f6f6f6;
  --nav-line:#e2e2e2;
  --nav-text:#555555;
  --navy:#1c2b63;
  --navy-deep:#101a45;
  --navy-light:#33457f;
  --green:#8dc63f;
  --green-dark:#7ab52f;
  --frame:#d9d9d9;
  --panel:#f0f0f0;
  --alert:#d9534f;
  --social:#c9d6ea;
}
*{box-sizing:border-box;margin:0;padding:0}
html,body{width:1200px;height:891px;overflow:hidden}
body{background:var(--page-bg);font-family:"Arimo",Arial,sans-serif;color:var(--ink)}
.site{position:absolute;left:131px;top:0;width:921px;height:891px;background:var(--white)}
.header{position:relative;height:98px}
.brand{position:absolute;left:21px;top:34px;display:flex;align-items:center;gap:8px}
.brand-dot{width:34px;height:34px;border-radius:50%;background:var(--green)}
.brand-name{font-size:34px;font-weight:400;color:var(--ink);letter-spacing:-0.5px}
.header-actions{position:absolute;right:22px;top:31px;display:flex;gap:14px}
.round-btn{width:42px;height:42px;border-radius:50%;background:var(--social);border:3px solid var(--white);box-shadow:0 1px 4px rgba(0,0,0,.35)}
.round-btn.work{background:var(--alert);color:var(--white);font-size:7px;font-weight:700;line-height:8px;display:flex;align-items:center;justify-content:center;text-align:center}
.nav{height:43px;background:var(--nav-bg);border-top:1px solid var(--nav-line);display:flex;align-items:center;padding-left:16px}
.nav a{font-size:13px;color:var(--nav-text);text-decoration:none;padding:0 17px;border-left:1px solid #999;line-height:20px}
.nav a:first-child{border-left:none;padding-left:12px}
.nav a .more{font-size:8px;margin-left:4px}
.hero{position:absolute;left:-2px;top:141px;width:923px;height:653px;overflow:hidden}
.hero-backdrop{position:absolute;inset:0;background:
  radial-gradient(ellipse at 90% 30%,rgba(60,50,40,.7),transparent 45%),
  linear-gradient(180deg,var(--navy-light) 0%,var(--navy) 55%,var(--navy-deep) 100%)}
.tag{position:absolute;left:216px;top:0;width:480px;height:59px;background:var(--green);clip-path:polygon(0 0,100% 0,93% 100%,7% 100%);color:var(--white);font-size:28px;text-align:center;line-height:60px}
.bulb{position:absolute;left:201px;top:87px}
.intro{position:absolute;left:82px;top:150px;width:260px;color:var(--white)}
.intro h2{font-size:17px;font-weight:700;text-align:center;margin-left:-10px;width:280px}
.intro p{font-size:13px;line-height:17px;margin:24px 0 0 21px;width:240px}
.intro .pitch{font-size:17px;font-weight:700;line-height:20px;margin-top:22px}
.hl{color:var(--green)}
.slide-frame{position:absolute;left:395px;top:139px;width:418px;height:237px;background:var(--frame);padding:6px;box-shadow:0 2px 8px rgba(0,0,0,.5)}
.slide-photo{width:100%;height:100%;background:linear-gradient(180deg,#151515 0%,#3a3a3a 60%,#6b6b6b 100%)}
.arrow{position:absolute;top:242px;width:0;height:0;border-top:11px solid transparent;border-bottom:11px solid transparent}
.arrow.prev{left:370px;border-right:11px solid var(--green)}
.arrow.next{left:825px;border-left:11px solid var(--green)}
.cta-strip{position:absolute;left:383px;top:398px;width:436px;height:29px;background:var(--green);clip-path:polygon(0 0,100% 0,97% 100%,3% 100%);color:var(--white);font-size:15px;font-weight:700;text-align:center;line-height:29px}
.cities{position:absolute;left:410px;top:445px;display:flex;gap:14px;list-style:none}
.cities a{color:var(--green);font-size:16px;font-weight:700;text-decoration:none;display:flex;align-items:center;gap:10px}
.cities a::before{content:"";border-top:7px solid transparent;border-bottom:7px solid transparent;border-left:8px solid var(--green)}
.campaign{position:absolute;left:0;width:923px;top:518px;text-align:center;color:var(--white)}
.campaign h1{font-size:44px;font-weight:700;letter-spacing:1px;line-height:50px;margin-left:-10px}
.campaign p{font-size:22px;margin-top:2px;margin-left:-10px}
.learn{position:absolute;left:343px;top:614px;width:232px;height:39px;background:var(--green);clip-path:polygon(0 0,100% 0,93% 100%,7% 100%);color:var(--white);font-size:22px;text-align:center;line-height:40px;text-decoration:none}
.content{position:absolute;left:21px;top:794px;width:880px;height:97px;background:var(--panel)}
</style>
</head>
<body>
<div class="site">
  <header class="header">
    <div class="brand"><span class="brand-dot"></span><span class="brand-name">VexaLume</span></div>
    <div class="header-actions">
      <a class="round-btn work">WORK<br>HERE</a>
      <a class="round-btn" aria-label="Social profile"></a>
      <a class="round-btn" aria-label="Professional network profile"></a>
      <a class="round-btn" aria-label="Microblog profile"></a>
    </div>
  </header>
  <nav class="nav">
    <a>Home</a>
    <a>Commercial<span class="more">▸</span></a>
    <a>Residential<span class="more">▸</span></a>
    <a>Field Services Division</a>
    <a>Education Center<span class="more">▸</span></a>
    <a>Our Company<span class="more">▸</span></a>
  </nav>
  <section class="hero">
    <div class="hero-backdrop" role="img" aria-label="Night city skyline with lit office towers and a moon over clouds"></div>
    <div class="tag">Save energy and enviroment</div>
    <svg class="bulb" width="30" height="46" viewBox="0 0 30 46" fill="none" stroke="#fff" stroke-width="1.8">
      <path d="M15 2a12 12 0 0 0-7 21.7c1.6 1.3 2 2.6 2 4.3v4h10v-4c0-1.7.4-3 2-4.3A12 12 0 0 0 15 2z"/>
      <path d="M10 36h10M10 40h10M12 44h6"/>
      <path d="M13 31v-9l2 2 2-2v9"/>
    </svg>
    <div class="intro">
      <h2>What is Quiet Horizon Initiative?</h2>
      <p>Wasted lighting that is left on at night time in office buildings not only produces unnecessary costs but also harms the enviroment. Light polution can be hazardous to the health of both humans and wildlife.</p>
      <p class="pitch">The Quiet Horizon Initiative is here to help you <span class="hl">reduce or eliminate wasted lighting</span> in your buildings.</p>
    </div>
    <span class="arrow prev"></span>
    <div class="slide-frame"><div class="slide-photo" role="img" aria-label="Black and white photo of downtown office towers at night with lit windows highlighted in green"></div></div>
    <span class="arrow next"></span>
    <div class="cta-strip">Are all those ligts needed? Check your buildings now:</div>
    <ul class="cities">
      <li><a>San Francisco</a></li>
      <li><a>New York City</a></li>
      <li><a>Los Angeles</a></li>
    </ul>
    <div class="campaign">
      <h1>QUIET HORIZON</h1>
      <p>Let your office sleep. <span class="hl">Save energy.</span></p>
    </div>
    <a class="learn">Learn More</a>
  </section>
  <div class="content"></div>
</div>
</body>
</html>
```